Thornwell Building Company - advertisement poster

I am looking to print some canvas signs to advertise my general contracting company, Thornwell Building Company. The sign will measure 6' long x 3' high so the size should match that ratio. I already have a logo icon, which is the Letter 'A' and some trees that I would like to incorporate, see attached. I would also like the to have the following information listed:
1) phone number: 472-318-6095
2) email: thornwellbuildingcompany@mailvistra.net
3) website: thornwellbuildingcompany.com
4) Lic#5386204
5) I want to use this text: "BUILD WITH THE T-CREW!"

The ad should be relatively simple and clean. Black and Green are my company colors. I am open to creative ideas!

Target Market(s)

People looking to renovate their homes

Industry/Entity Type

Construction

Colors
59FF00
82FF00
B8FF75
E3FFCB
F4FFEA

Requirements
Must have
• Must have my company logo
Should not have
• No photos or complex graphics

```html
<!DOCTYPE html>
<html lang="en">
<head>
<meta charset="utf-8">
<title>Thornwell Building Company – Sign</title>
<link href="https://fonts.googleapis.com/css2?family=Montserrat:wght@500;600;800;900&family=Michroma&display=swap" rel="stylesheet">
<style>
  :root {
    --stage: #8a8a8a;
    --green: #72b447;
    --green-dark: #2d5a1e;
    --green-band: #234a15;
    --black: #000000;
    --white: #ffffff;
    --sketch-a: #8cc24f;
    --sketch-b: #9fcb55;
  }
  * { margin: 0; padding: 0; box-sizing: border-box; }
  html, body { width: 1200px; height: 747px; overflow: hidden; }
  body { background: var(--stage); position: relative; font-family: "Montserrat", sans-serif; }

  .sign {
    position: absolute; left: 69px; top: 108px;
    width: 1062px; height: 531px; overflow: hidden;
    background: var(--black);
  }
  .sign-shapes { position: absolute; inset: 0; }

  .headline {
    position: absolute; left: 34px; top: 40px;
    font-family: "Montserrat", sans-serif; font-weight: 900;
    font-size: 58px; line-height: 52px; letter-spacing: -1px;
  }
  .headline .dark { color: var(--black); }
  .headline .light { color: var(--white); }

  .house-sketch {
    position: absolute; left: 30px; top: 268px; width: 330px; height: 187px;
    background: radial-gradient(ellipse at 50% 55%, var(--sketch-b) 0%, var(--sketch-a) 55%, rgba(114,180,71,0) 80%);
    opacity: .8;
  }

  .license {
    position: absolute; left: 37px; top: 459px;
    color: var(--white); font-weight: 600; font-size: 26px; letter-spacing: .2px;
  }

  .brand { position: absolute; left: 480px; top: 40px; width: 400px; text-align: center; }
  .brand-mark {
    width: 58px; height: 58px; margin: 18px auto 0; background: var(--green);
  }
  .estd {
    position: absolute; top: 70px; font-family: "Michroma", sans-serif;
    color: var(--white); font-size: 12px; letter-spacing: 4px;
    border-top: 1.5px solid var(--green); border-bottom: 1.5px solid var(--green);
    padding: 5px 0 5px 4px; width: 62px; text-align: center;
  }
  .estd.left { left: 47px; }
  .estd.right { right: 47px; }
  .brand-name {
    margin-top: 50px; font-family: "Michroma", sans-serif; color: var(--white);
    font-size: 40px; line-height: 1; letter-spacing: 1px;
  }
  .brand-sub {
    margin-top: 14px; font-family: "Michroma", sans-serif; color: var(--white);
    font-size: 19px; letter-spacing: 9px;
  }

  .contacts { position: absolute; left: 0; top: 0; }
  .contact {
    position: absolute; display: flex; align-items: center; gap: 26px;
    color: var(--white); white-space: nowrap;
  }
  .contact svg { flex: none; }
  .contact.phone { left: 433px; top: 367px; font-weight: 600; font-size: 27px; }
  .contact.email { left: 447px; top: 410px; font-weight: 500; font-size: 23px; gap: 22px; }
  .contact.web { left: 458px; top: 455px; font-weight: 500; font-size: 25px; gap: 22px; }
</style>
</head>
<body>
  <section class="sign">
    <svg class="sign-shapes" width="1062" height="531" viewBox="0 0 1062 531">
      <defs>
        <linearGradient id="edgeShade" x1="0" x2="1" y1="0" y2="0">
          <stop offset="0" stop-color="#1e3d14"/>
          <stop offset="1" stop-color="#1e3d14" stop-opacity="0"/>
        </linearGradient>
        <clipPath id="stripeClip"><polygon points="966,0 1062,0 1062,386"/></clipPath>
      </defs>
      <polygon points="0,0 289,0 426,531 0,531" fill="var(--green)"/>
      <polygon points="289,0 308,0 445,531 426,531" fill="url(#edgeShade)"/>
      <rect x="0" y="455" width="490" height="46" fill="var(--green-band)"/>
      <polygon points="426,0 1062,0 1062,531 433,531 300,0" fill="none"/>
      <polygon points="308,0 1062,0 1062,531 445,531" fill="var(--black)"/>
      <g clip-path="url(#stripeClip)">
        <rect x="940" y="0" width="122" height="386" fill="var(--green-dark)"/>
        <g fill="var(--green)">
          <rect x="940" y="0" width="122" height="11"/>
          <rect x="940" y="24" width="122" height="11"/>
          <rect x="940" y="48" width="122" height="11"/>
          <rect x="940" y="72" width="122" height="11"/>
          <rect x="940" y="96" width="122" height="11"/>
          <rect x="940" y="120" width="122" height="11"/>
          <rect x="940" y="144" width="122" height="11"/>
          <rect x="940" y="168" width="122" height="11"/>
          <rect x="940" y="192" width="122" height="11"/>
          <rect x="940" y="216" width="122" height="11"/>
          <rect x="940" y="240" width="122" height="11"/>
          <rect x="940" y="264" width="122" height="11"/>
          <rect x="940" y="288" width="122" height="11"/>
          <rect x="940" y="312" width="122" height="11"/>
          <rect x="940" y="336" width="122" height="11"/>
          <rect x="940" y="360" width="122" height="11"/>
        </g>
      </g>
      <polyline points="429,352 414,310 1062,310" fill="none" stroke="var(--green)" stroke-width="1.2"/>
    </svg>

    <h1 class="headline">
      <span class="dark">BUILD</span><br>
      <span class="light">WITH</span><br>
      <span class="light">THE</span><br>
      <span class="dark">T-CREW!</span>
    </h1>

    <div class="house-sketch" role="img" aria-label="Faint green wireframe drawing of a house frame"></div>

    <p class="license">License # 5386204</p>

    <div class="brand">
      <div class="brand-mark"></div>
      <span class="estd left">ESTD</span>
      <span class="estd right">2020</span>
      <div class="brand-name">THORNWELL</div>
      <div class="brand-sub">BUILDING COMPANY</div>
    </div>

    <div class="contacts">
      <div class="contact phone">
        <svg width="24" height="24" viewBox="0 0 24 24" fill="none" stroke="var(--green)" stroke-width="1.8" stroke-linejoin="round">
          <path d="M5 2h4l2 5-2.5 1.5a11 11 0 0 0 7 7L17 13l5 2v4a2 2 0 0 1-2 2A18 18 0 0 1 3 4a2 2 0 0 1 2-2z"/>
        </svg>
        <span>472.318.6095</span>
      </div>
      <div class="contact email">
        <svg width="26" height="20" viewBox="0 0 26 20" fill="none" stroke="var(--green)" stroke-width="1.8">
          <rect x="1" y="1" width="24" height="18"/>
          <path d="M1 1l12 10L25 1M1 19l9-8M25 19l-9-8"/>
        </svg>
        <span>thornwellbuildingcompany@mailvistra.net</span>
      </div>
      <div class="contact web">
        <svg width="28" height="28" viewBox="0 0 28 28" fill="none" stroke="var(--green)" stroke-width="1.8">
          <circle cx="14" cy="14" r="12.5"/>
          <ellipse cx="14" cy="14" rx="5.5" ry="12.5"/>
          <path d="M1.5 14h25M3.5 8h21M3.5 20h21"/>
        </svg>
        <span>thornwellbuildingcompany.com</span>
      </div>
    </div>
  </section>
</body>
</html>
```